Business Card Design

We need a business card design for a Non-Profit Christian Based Organization located in Milford, Pa.
Alder Ridge Helping Harbor
Is a Christ-centered organization dedicated to providing compassion and hope to homeless or near homeless, families and individuals, by meeting their basic and urgent need of food, clothing and shelter.
Updates
the logo is black and white
and must add the color green some where 00400
Industry/Entity Type
Clothing
Contact Information for Business Card
Alder Ridge Helping Harbor
P.O. Box 287
Milord, Pa 18337
Phone: (570) 413-CARE(2273)
Toll Free: (855) 413-CARE
email:Info@alderridgehh.org
email:Careline@alderridgehh.org
Our organization already has a logo.
Front of card:
Is a Christ-centered organization dedicated to providing compassion and hope to homeless or near homes, families and individual by meeting their basic and urgent need of food, clothing and shelter.(this is our Mission Statement)
On back of card:
'I was hungry and you gave me something to eat;
"I was thirsty and you gave me something to drink;
"I was a stranger and you invited me in."
Matthew 25:35
Color: Logo is black and white
Background color I would like a bright light green 00ff00(close to that)
I attached a sample of what I created on Quill Press but, I don't like the color green, nor the design (but I just wanted to give you and Idea of the Logo and Alder Ridge (one line) Helping Harbor (second line) in a different font thank you
Delia Rostova
Pr/Board of Directors

```html
<!DOCTYPE html>
<html lang="en">
<head>
<meta charset="utf-8">
<title>Alder Ridge Helping Harbor – Business Card Back</title>
<link rel="stylesheet" href="https://fonts.googleapis.com/css2?family=Pinyon+Script&display=swap">
<style>
  :root {
    --card-green: #afd039;
    --ink: #141414;
    --emblem-tone: #1c1c1c;
    --frame: #000000;
  }
  html, body {
    margin: 0;
    padding: 0;
    width: 1200px;
    height: 702px;
    overflow: hidden;
    background: #ffffff;
  }
  .card {
    position: relative;
    width: 1200px;
    height: 702px;
    box-sizing: border-box;
    background: var(--card-green);
    border: 3px solid var(--frame);
    font-family: "Pinyon Script", cursive;
    color: var(--ink);
  }
  .emblem {
    position: absolute;
    left: 570px;
    top: 60px;
    width: 106px;
    height: 162px;
    border-radius: 6px;
    background: var(--emblem-tone);
  }
  .verse {
    position: absolute;
    left: 0;
    right: 0;
    top: 234px;
    margin: 0;
    padding-left: 80px;
    text-align: center;
    font-size: 37px;
    line-height: 63px;
    font-weight: 400;
  }
  .verse-line {
    display: block;
  }
  .verse-ref {
    position: absolute;
    left: 0;
    right: 0;
    top: 430px;
    margin: 0;
    padding-left: 80px;
    text-align: center;
    font-size: 37px;
    line-height: 52px;
    font-weight: 400;
  }
  .org-name {
    position: absolute;
    left: 0;
    right: 0;
    top: 540px;
    margin: 0;
    padding-left: 70px;
    text-align: center;
    font-size: 38px;
    line-height: 46px;
    font-weight: 400;
  }
  .org-name span {
    display: block;
  }
</style>
</head>
<body>
  <main class="card">
    <div class="emblem" role="img" aria-label="Organization emblem area, black and white"></div>

    <p class="verse">
      <span class="verse-line">"I was hungry and you gave me something to eat;</span>
      <span class="verse-line">I was thirsty and you gave me something to drink;</span>
      <span class="verse-line">I was a stranger and you invited me in."</span>
    </p>
    <p class="verse-ref">Matthew 25:35</p>

    <h1 class="org-name">
      <span>Alder Ridge</span>
      <span>Helping Harbor</span>
    </h1>
  </main>
</body>
</html>
```